Vantel Trophy Design Project

We have just won an award for customer service and would like to tell our users about how great we are!!

The award is the 3013 Brindlemoor Vantel Trophy for excellence in Customer relations.

We have a in house made banner currently on our home page slider (www.tarvelloshop.com.au) but we would prefer something more professional.

```html
<!DOCTYPE html>
<html lang="en">
<head>
<meta charset="utf-8">
<title>2013 Brindlemoor Vantel Trophy – Highly Recommended</title>
<link rel="stylesheet" href="https://fonts.googleapis.com/css2?family=Cormorant+Garamond:ital,wght@0,500;1,500&family=Cinzel:wght@400&display=swap">
<style>
  :root {
    --fabric-dark: #7f7f0c;
    --fabric-mid: #9c9b17;
    --fabric-light: #b3b12a;
    --badge-fill: #a9a71f;
    --badge-glow: #d9d77a;
    --ink: #111106;
    --bar-text: #dedb8c;
  }
  * { margin: 0; padding: 0; box-sizing: border-box; }
  html, body { width: 1200px; height: 591px; overflow: hidden; background: var(--fabric-mid); }
  .banner { position: relative; width: 1200px; height: 591px; overflow: hidden; }
  .fabric-backdrop {
    position: absolute; inset: 0;
    background:
      radial-gradient(ellipse at 30% 25%, var(--fabric-light) 0%, transparent 55%),
      radial-gradient(ellipse at 20% 90%, var(--fabric-dark) 0%, transparent 60%),
      linear-gradient(135deg, var(--fabric-mid) 0%, var(--fabric-dark) 100%);
  }
  .award-badge {
    position: absolute; left: 664px; top: 19px; width: 490px; height: 546px;
    background: var(--badge-fill);
    box-shadow: inset 0 0 22px 6px var(--badge-glow), 10px 12px 18px rgba(20,20,0,0.6);
    color: var(--ink);
  }
  .award-year {
    position: absolute; left: 44px; top: 28px;
    font-family: "Cormorant Garamond", serif; font-weight: 500; font-size: 58px; line-height: 1;
  }
  .award-name {
    position: absolute; left: 44px; top: 88px; width: 420px;
    font-family: "Cormorant Garamond", serif; font-weight: 500; font-size: 76px; line-height: 0.98;
  }
  .award-rule {
    position: absolute; left: 44px; top: 250px; width: 420px; height: 3px; background: var(--ink);
  }
  .award-kind {
    position: absolute; left: 44px; top: 262px; width: 420px;
    font-family: "Cinzel", serif; font-size: 38px; line-height: 1;
    display: flex; justify-content: space-between;
  }
  .award-level {
    position: absolute; left: 44px; top: 336px; width: 420px; height: 75px;
    background: var(--ink); color: var(--bar-text);
    display: flex; align-items: center; justify-content: center;
    font-family: "Cormorant Garamond", serif; font-style: italic; font-weight: 500; font-size: 46px;
  }
  .award-category {
    position: absolute; left: 20px; top: 470px; width: 450px; text-align: center;
    font-family: "Cormorant Garamond", serif; font-style: italic; font-weight: 500; font-size: 31px;
  }
</style>
</head>
<body>
<main class="banner">
  <div class="fabric-backdrop" role="img" aria-label="Close-up photograph of olive-green woven fabric texture"></div>
  <section class="award-badge" aria-label="2013 Brindlemoor Vantel Trophy, Highly Recommended, Excellence in Customer Service">
    <p class="award-year">2013</p>
    <h1 class="award-name">Brindlemoor<br>Vantel</h1>
    <div class="award-rule"></div>
    <p class="award-kind"><span>T</span><span>R</span><span>O</span><span>P</span><span>H</span><span>Y</span></p>
    <p class="award-level">Highly Recommended</p>
    <p class="award-category">Excellence in Customer Service</p>
  </section>
</main>
</body>
</html>
```